I have a logo and need to design the business card and stationery.
Updates

The uploaded logo image named as GREYHAVEN CONSTRUCTION which is to be replaced to GREYHAVEN CONTRACTS. Kindly add below details and submit the designs- Company name- Greyhaven Engineering Contracts LLP Name & Post- Kunal Mehra (Designated Partner) Address- Block No.317, Wing C, Tulsi Trade Plaza, Lokhand Marg, Varun Industrial Park, Goregaon(E), Mumbai - 400 063 Contact- +91 97410 58723 Email- kunalmehra@examplemail.com Website- www.greyhavencontracts.example Contact for Letterhead- +91-22-28145597

Hi Tanvir Rahman, We are liking your Design #41927506. We have suggested some changes which are mentioned in feedback. Kindly revert with it asap to finalize this design.

Colors

Designer to choose colors to be used in the design.

```html
<!DOCTYPE html>
<html lang="en">
<head>
<meta charset="utf-8">
<title>Greyhaven Contracts – Letterhead</title>
<link rel="stylesheet" href="https://fonts.googleapis.com/css2?family=Open+Sans:wght@400;600;700&family=Orbitron:wght@700&display=swap">
<style>
  :root {
    --backdrop: #e4e4e4;
    --paper: #ffffff;
    --ink: #2b2b2b;
    --ink-soft: #555555;
    --bar-dark: #2f2f2f;
    --bar-mid: #4a4a4a;
    --sig-tone: #ececec;
  }
  * { margin: 0; padding: 0; box-sizing: border-box; }
  html, body {
    width: 1040px; height: 1200px; overflow: hidden;
    background: var(--backdrop);
    font-family: "Open Sans", Arial, sans-serif;
    color: var(--ink-soft);
  }
  .letterhead {
    position: absolute; left: 80px; top: 35px;
    width: 800px; height: 1027px;
    background: var(--paper);
    box-shadow: 0 2px 8px rgba(0,0,0,.25);
    transform: scale(1.1); transform-origin: top left;
  }
  .brand {
    position: absolute; right: 82px; top: 31px;
    display: flex; flex-direction: column; align-items: flex-end;
  }
  .brand-square {
    width: 82px; height: 82px; background: var(--ink);
    margin-right: 88px; margin-bottom: 12px;
  }
  .brand-name {
    font-weight: 700; font-size: 21px; line-height: 22px;
    letter-spacing: 1px; color: var(--ink); text-align: right;
  }
  .letter {
    position: absolute; left: 75px; top: 244px; width: 645px;
    font-size: 13px; line-height: 23px;
  }
  .letter p { margin-bottom: 14px; }
  .recipient { line-height: 15.5px; margin-bottom: 30px !important; }
  .date { margin-bottom: 14px !important; }
  .body-text { text-align: justify; margin-bottom: 23px !important; }
  .closing { margin-top: 40px; }
  .signature {
    display: block; width: 185px; height: 22px;
    background: linear-gradient(90deg, var(--sig-tone), #f6f6f6);
    margin: 8px 0 6px;
  }
  .signer-name { font-size: 15px; font-weight: 600; color: var(--ink); line-height: 20px; }
  .signer-role { line-height: 24px; }
  .contact-strip { position: absolute; left: 56px; bottom: 0; width: 355px; }
  .contact-rule { height: 10px; background: var(--bar-mid); margin-bottom: 8px; }
  .contact-box {
    height: 48px; background: var(--bar-dark);
    display: flex; align-items: center; padding-left: 31px; gap: 8px;
    color: #fff; font-family: "Orbitron", "Arial Black", sans-serif;
    font-weight: 700; font-size: 19px; letter-spacing: 1.5px;
  }
</style>
</head>
<body>
<article class="letterhead">
  <header class="brand">
    <div class="brand-square"></div>
    <div class="brand-name">GREYHAVEN<br>CONTRACTS</div>
  </header>

  <section class="letter">
    <p class="date">Issuing Date: May 5, 2018</p>
    <p class="recipient">Name Of Employee Mr. XYZABC<br>Address of Employee<br>Address Line 2 etc..</p>
    <p>Dear Mr.XYZABC</p>
    <p class="body-text">Lorem Ipsum has been the industry's standard dummy text ever since the 1500s, when an unknown printer took a galley of type and scrambled it to make a type specimen book. It has survived not only five centuries, but also the leap into electronic typesetting, remaining essentially unchanged. It was popularised in the 1960s with the release of Letraset sheets containing Lorem Ipsum passages, and more recently with desktop publishing software like Aldus PageMaker including versions of Lorem Ipsum.</p>
    <p class="body-text">Lorem Ipsum is simply dummy text of the printing and typesetting industry. Lorem Ipsum has been the industry's standard dummy text ever since the 1500s, when an unknown printer took a galley of type and scrambled it to make a type specimen book.</p>
    <p class="body-text">It has survived not only five centuries, but also the leap into electronic typesetting, remaining essentially unchanged. It was popularised in the 1960s with the release of Letraset sheets containing Lorem IpsumIpsum passages.</p>

    <div class="closing">
      <p style="margin:0">Yours Sincerely</p>
      <span class="signature" role="img" aria-label="Handwritten signature of Rohan Desai"></span>
      <p class="signer-name" style="margin:0">Rohan Desai</p>
      <p class="signer-role" style="margin:0">Managing Director</p>
    </div>
  </section>

  <footer class="contact-strip">
    <div class="contact-rule"></div>
    <div class="contact-box">
      <svg width="28" height="28" viewBox="0 0 28 28" aria-hidden="true">
        <rect x="1" y="1" width="26" height="26" rx="4" fill="none" stroke="#fff" stroke-width="2"/>
        <path d="M9 7c-1.5 1-2 2.5-1.5 4.5 1 4 4.5 8 8.5 9.5 2 .5 3.5 0 4.5-1.5l-2.5-2.5-2 1c-2-1-4-3-5-5l1-2z" fill="#fff"/>
      </svg>
      <span>+91 97410 58723</span>
    </div>
  </footer>
</article>
</body>
</html>
```